We have a cheerleading competition on Sunday the 30 and I want to encourage parent assistance, support and participation!
Updates

1. Please add:
    Cheer Championship (instead of Cheerleading Competition)

2. Banner: Let's support our Cheerleaders!

Under Banner have the Date in big

Before the Location add:  Joins us at:

Thank you all for your designs and taking the time to submit them. I greatly appreciate them and they were all lovely. I could only pick one though! Hope to have you again on my next project.

Regards, Marisa

Industry/Entity Type

It Support

Requirements
Must have
• Flyer should be 1/2 of an A4 page. kid friendly. The cheerleaders are 6-13 yrs old.
The colors Burgundy, Gold (yellow) and White - It should have the team Eagle design on it. Tarpon Ridge Falcons

Simple design. It will contain an address, times and dates.

should have all of the following information:

Date: Sunday - October 30th 2011
Location: Harbor Crest Arena at the Pellham Coast College
3870 Kestrel Lane
Palm Hollow, FL 33920
Time: Tickets on sale 8:30AM - Doors Open 9:00AM Starts: 10:00AM
Prices: Adults $10.00 Children $5.00 - Cash Only

```html
<!DOCTYPE html>
<html lang="en">
<head>
<meta charset="utf-8">
<title>Cheer Championship Flyer – Tarpon Ridge Falcons</title>
<link rel="stylesheet" href="https://fonts.googleapis.com/css2?family=Arimo:wght@400;700&family=Lilita+One&display=swap">
<style>
  :root {
    --cheer-red: #d8202a;
    --cheer-burgundy: #a1131c;
    --cheer-deep: #7a0f18;
    --cheer-gold: #f6b228;
    --cheer-gold-light: #fcd36a;
    --paper: #ffffff;
    --ink: #1b1b1b;
    --frame: #4a4a4a;
    --shadow-grey: #5c5c5c;
  }

  * { box-sizing: border-box; margin: 0; padding: 0; }

  html, body {
    width: 850px;
    height: 1200px;
    overflow: hidden;
    background: var(--paper);
    font-family: "Arimo", Arial, sans-serif;
    color: var(--ink);
  }

  .sheet { position: relative; width: 850px; height: 1200px; }

  .sheet-panel {
    position: absolute;
    left: 3px;
    width: 844px;
    height: 592px;
    border: 1px solid var(--frame);
    background: var(--paper);
    overflow: hidden;
  }
  .sheet-panel--portrait { top: 3px; }
  .sheet-panel--landscape { top: 603px; }

  .flyer { position: absolute; left: 0; top: 0; overflow: hidden; background: var(--paper); }
  .flyer--portrait {
    width: 592px;
    height: 844px;
    transform-origin: top left;
    transform: translate(844px, 0) rotate(90deg);
  }
  .flyer--landscape { width: 844px; height: 592px; }

  .swooshes { position: absolute; inset: 0; width: 100%; height: 100%; }
  .swoosh { fill: var(--cheer-gold); }
  .swoosh--light { fill: var(--cheer-gold-light); }

  .cheerleader-art {
    position: absolute;
    border-radius: 46% 46% 40% 40%;
    background: radial-gradient(ellipse at 50% 40%, var(--cheer-red) 0%, var(--cheer-burgundy) 75%, rgba(161,19,28,0) 100%);
    opacity: 0.92;
  }

  .title-word {
    position: absolute;
    font-family: "Lilita One", "Arial Black", sans-serif;
    font-weight: 400;
    color: var(--cheer-red);
    line-height: 1;
    white-space: nowrap;
    letter-spacing: 1px;
    text-shadow:
      -3px -3px 0 var(--paper), 3px -3px 0 var(--paper),
      -3px 3px 0 var(--paper), 3px 3px 0 var(--paper),
      0 -4px 0 var(--paper), 0 4px 0 var(--paper),
      -4px 0 0 var(--paper), 4px 0 0 var(--paper),
      6px 6px 0 var(--shadow-grey), 7px 7px 2px rgba(0,0,0,0.45);
  }

  .slogan-banner { position: absolute; overflow: visible; }
  .slogan-banner__flag { fill: var(--cheer-red); }
  .slogan-banner__fold { fill: var(--cheer-deep); }
  .slogan-banner__text {
    font-family: "Lilita One", "Arial Black", sans-serif;
    fill: var(--paper);
    letter-spacing: 0.5px;
  }

  .promo-tag {
    position: absolute;
    border-radius: 14px;
    background: linear-gradient(160deg, var(--cheer-red) 0%, var(--cheer-burgundy) 100%);
    color: var(--paper);
    font-weight: 700;
    text-align: center;
    box-shadow: 4px 6px 8px rgba(0,0,0,0.35);
    display: flex;
    flex-direction: column;
    justify-content: center;
    line-height: 1.3;
    white-space: nowrap;
  }
  .promo-tag__lead { font-size: 16px; }
  .promo-tag__line { font-size: 14px; }
  .promo-tag__price { font-size: 18px; }

  .event-date { position: absolute; text-align: center; color: var(--cheer-red); font-weight: 700; }
  .event-date__day { font-size: 36px; line-height: 1.05; }
  .event-date__full { font-size: 19px; }

  .schedule { position: absolute; font-weight: 700; color: var(--ink); }
  .schedule__heading { color: var(--cheer-red); font-size: 18px; text-align: center; margin-bottom: 6px; }
  .schedule__row {
    display: flex;
    justify-content: space-between;
    font-size: 16px;
    line-height: 22px;
    white-space: nowrap;
  }

  .pricing { position: absolute; text-align: center; color: var(--cheer-red); font-weight: 700; white-space: nowrap; }
  .pricing__heading { font-size: 18px; margin-bottom: 2px; }
  .pricing__row { font-size: 14px; line-height: 1.45; }

  .venue { position: absolute; text-align: center; font-weight: 700; white-space: nowrap; }
  .venue__invite { color: var(--cheer-red); font-size: 19px; margin-bottom: 8px; }
  .venue__box {
    border: 3px solid var(--cheer-red);
    border-radius: 16px;
    padding: 8px 8px;
    color: var(--cheer-red);
    background: var(--paper);
  }
  .venue__box--gold { border-color: var(--cheer-gold); color: var(--ink); }
  .venue__name { font-size: 15px; line-height: 1.3; }
  .venue__street { font-size: 21px; line-height: 1.3; }
  .venue__city { font-size: 15px; line-height: 1.35; }

  .team-mark { position: absolute; display: flex; flex-direction: column; align-items: center; gap: 8px; }
  .team-mark__dot { width: 54px; height: 54px; border-radius: 50%; background: var(--cheer-deep); }
  .team-mark__name {
    font-family: "Arimo", Arial, sans-serif;
    font-weight: 700;
    font-size: 13px;
    color: var(--ink);
    white-space: nowrap;
  }

  /* Portrait layout */
  .flyer--portrait .cheerleader-art--top { left: 392px; top: 62px; width: 150px; height: 135px; }
  .flyer--portrait .cheerleader-art--side { left: 30px; top: 378px; width: 132px; height: 138px; }
  .flyer--portrait .title-word--cheer { left: 138px; top: 118px; font-size: 100px; transform: rotate(-4deg); }
  .flyer--portrait .title-word--championship { left: 40px; top: 214px; font-size: 84px; transform: rotate(-4deg); }
  .flyer--portrait .slogan-banner { left: 58px; top: 296px; width: 500px; height: 78px; }
  .flyer--portrait .event-date { left: 180px; top: 392px; width: 240px; }
  .flyer--portrait .venue { left: 282px; top: 478px; width: 286px; }
  .flyer--portrait .schedule-wrap { position: absolute; left: 318px; top: 648px; width: 252px; }
  .flyer--portrait .schedule-wrap .schedule { position: static; }
  .flyer--portrait .schedule__box { border: 3px solid var(--cheer-gold); border-radius: 18px; padding: 10px 14px; }
  .flyer--portrait .schedule__row { font-size: 17px; line-height: 24px; }
  .flyer--portrait .pricing { left: 50px; top: 520px; width: 210px; }
  .flyer--portrait .promo-tag { left: 22px; top: 622px; width: 214px; height: 96px; transform: rotate(-5deg); }
  .flyer--portrait .promo-tag__lead { font-size: 14px; }
  .flyer--portrait .promo-tag__line { font-size: 13px; }
  .flyer--portrait .promo-tag__price { font-size: 16px; }
  .flyer--portrait .team-mark { left: 30px; top: 738px; width: 200px; }

  /* Landscape layout */
  .flyer--landscape .team-mark { left: 50px; top: 36px; width: 150px; }
  .flyer--landscape .team-mark__dot { width: 62px; height: 62px; }
  .flyer--landscape .cheerleader-art--top { left: 556px; top: 38px; width: 100px; height: 112px; }
  .flyer--landscape .cheerleader-art--side { left: 186px; top: 376px; width: 98px; height: 176px; }
  .flyer--landscape .title-word--cheer { left: 276px; top: 58px; font-size: 90px; transform: rotate(-3deg); }
  .flyer--landscape .title-word--championship { left: 170px; top: 136px; font-size: 82px; transform: rotate(-3deg); }
  .flyer--landscape .slogan-banner { left: 250px; top: 206px; width: 476px; height: 74px; }
  .flyer--landscape .promo-tag { left: 12px; top: 264px; width: 248px; height: 108px; transform: rotate(-4deg); }
  .flyer--landscape .promo-tag__lead { font-size: 15px; }
  .flyer--landscape .promo-tag__line { font-size: 13.5px; }
  .flyer--landscape .promo-tag__price { font-size: 17px; }
  .flyer--landscape .event-date { left: 300px; top: 300px; width: 228px; }
  .flyer--landscape .schedule { left: 322px; top: 376px; width: 202px; }
  .flyer--landscape .pricing { left: 300px; top: 484px; width: 248px; }
  .flyer--landscape .venue { left: 578px; top: 282px; width: 228px; }
</style>
</head>
<body>
<main class="sheet">

  <section class="sheet-panel sheet-panel--portrait" aria-label="Cheer Championship flyer, portrait edition">
    <article class="flyer flyer--portrait">
      <svg class="swooshes" viewBox="0 0 592 844" preserveAspectRatio="none" aria-hidden="true">
        <path class="swoosh" d="M0,0 L190,0 C150,70 80,160 0,220 Z"/>
        <path class="swoosh--light" d="M0,250 C90,200 170,120 215,0 L240,0 C200,140 110,230 0,280 Z"/>
        <path class="swoosh" d="M380,0 L592,0 L592,170 C540,110 470,50 380,0 Z"/>
        <path class="swoosh" d="M0,515 C120,600 220,720 262,844 L222,844 C180,740 100,630 0,560 Z"/>
        <path class="swoosh" d="M592,760 C540,790 500,815 470,844 L592,844 Z"/>
      </svg>

      <div class="cheerleader-art cheerleader-art--top" role="img" aria-label="Red silhouette of a jumping cheerleader with pom-poms"></div>
      <div class="cheerleader-art cheerleader-art--side" role="img" aria-label="Red silhouette of a cheerleader leaping with pom-poms"></div>

      <h1 class="title-word title-word--cheer">Cheer</h1>
      <h1 class="title-word title-word--championship">Championship</h1>

      <svg class="slogan-banner" viewBox="0 0 500 78" aria-label="Let's support our Cheerleaders!">
        <path class="slogan-banner__fold" d="M10,40 L30,22 L30,70 Z"/>
        <path class="slogan-banner__flag" d="M20,28 C150,10 320,50 490,8 L480,50 C320,88 150,50 24,70 Z"/>
        <text class="slogan-banner__text" x="250" y="52" font-size="25" text-anchor="middle" transform="rotate(-3 250 45)">Let's support our Cheerleaders!</text>
      </svg>

      <div class="event-date">
        <p class="event-date__day">Sunday</p>
        <p class="event-date__full">October 30th 2011</p>
      </div>

      <div class="venue">
        <p class="venue__invite">Join us at:</p>
        <div class="venue__box venue__box--gold">
          <p class="venue__name">Harbor Crest Arena at<br>the Pellham Coast College</p>
          <p class="venue__street">3870 Kestrel Lane</p>
          <p class="venue__city">Palm Hollow, FL 33920</p>
        </div>
      </div>

      <div class="schedule-wrap">
        <div class="schedule">
          <p class="schedule__heading">Time:</p>
          <div class="schedule__box">
            <p class="schedule__row"><span>Tickets on sale</span><span>8:30AM</span></p>
            <p class="schedule__row"><span>Doors Open</span><span>9:00AM</span></p>
            <p class="schedule__row"><span>Starts:</span><span>10:00AM</span></p>
          </div>
        </div>
      </div>

      <div class="pricing">
        <p class="pricing__heading">Prices:</p>
        <p class="pricing__row">Adults $10.00</p>
        <p class="pricing__row">Children $5.00 - Cash Only</p>
      </div>

      <div class="promo-tag">
        <p class="promo-tag__lead">RALLY Coaches &amp; Players</p>
        <p class="promo-tag__line">Wear your Falcons Jersey</p>
        <p class="promo-tag__price">&amp; get in for $5 !</p>
      </div>

      <div class="team-mark">
        <span class="team-mark__dot" aria-hidden="true"></span>
        <span class="team-mark__name">Tarpon Ridge Falcons</span>
      </div>
    </article>
  </section>

  <section class="sheet-panel sheet-panel--landscape" aria-label="Cheer Championship flyer, landscape edition">
    <article class="flyer flyer--landscape">
      <svg class="swooshes" viewBox="0 0 844 592" preserveAspectRatio="none" aria-hidden="true">
        <path class="swoosh" d="M470,0 L560,0 C660,40 770,110 844,190 L844,250 C760,140 630,50 470,0 Z"/>
        <path class="swoosh--light" d="M640,0 L700,0 C760,30 810,60 844,90 L844,125 C790,80 720,35 640,0 Z"/>
        <path class="swoosh" d="M0,372 C110,390 200,460 236,592 L186,592 C150,480 90,425 0,415 Z"/>
        <path class="swoosh" d="M0,450 C60,470 100,520 118,592 L84,592 C66,530 36,492 0,482 Z"/>
        <path class="swoosh" d="M560,592 C630,515 730,465 844,452 L844,500 C750,515 680,548 636,592 Z"/>
        <path class="swoosh--light" d="M720,592 C760,560 800,540 844,532 L844,560 C810,566 784,578 764,592 Z"/>
      </svg>

      <div class="team-mark">
        <span class="team-mark__dot" aria-hidden="true"></span>
        <span class="team-mark__name">Tarpon Ridge Falcons</span>
      </div>

      <div class="cheerleader-art cheerleader-art--top" role="img" aria-label="Red silhouette of a jumping cheerleader with pom-poms"></div>
      <div class="cheerleader-art cheerleader-art--side" role="img" aria-label="Red silhouette of a cheerleader leaping with pom-poms"></div>

      <h1 class="title-word title-word--cheer">Cheer</h1>
      <h1 class="title-word title-word--championship">Championship</h1>

      <svg class="slogan-banner" viewBox="0 0 476 74" aria-label="Let's support our Cheerleaders!">
        <path class="slogan-banner__fold" d="M8,38 L28,20 L28,68 Z"/>
        <path class="slogan-banner__flag" d="M18,26 C140,8 300,46 468,6 L458,48 C300,84 140,48 22,68 Z"/>
        <text class="slogan-banner__text" x="240" y="50" font-size="24" text-anchor="middle" transform="rotate(-3 240 44)">Let's support our Cheerleaders!</text>
      </svg>

      <div class="promo-tag">
        <p class="promo-tag__lead">RALLY Coaches &amp; Players</p>
        <p class="promo-tag__line">Wear your Falcons Jersey</p>
        <p class="promo-tag__price">&amp; get in for $5 !</p>
      </div>

      <div class="event-date">
        <p class="event-date__day">Sunday</p>
        <p class="event-date__full">October 30th 2011</p>
      </div>

      <div class="schedule">
        <p class="schedule__heading">Time:</p>
        <p class="schedule__row"><span>Tickets on sale</span><span>8:30AM</span></p>
        <p class="schedule__row"><span>Doors Open</span><span>9:00AM</span></p>
        <p class="schedule__row"><span>Starts:</span><span>10:00AM</span></p>
      </div>

      <div class="pricing">
        <p class="pricing__heading">Prices:</p>
        <p class="pricing__row">Adults $10.00</p>
        <p class="pricing__row">Children $5.00 - Cash Only</p>
      </div>

      <div class="venue">
        <p class="venue__invite">Join us at:</p>
        <div class="venue__box">
          <p class="venue__name">Harbor Crest Arena at<br>the Pellham Coast College</p>
          <p class="venue__street">3870 Kestrel Lane</p>
          <p class="venue__city">Palm Hollow, FL 33920</p>
        </div>
      </div>
    </article>
  </section>

</main>
</body>
</html>
```